Anzeigengestaltung für Brötchen- und Brotlieferant
Zielgruppe
Wir beliefern Privatkunden Freitag, Samstag und Sonntag mit Brötchen / Broten und suchen ein Design für eine Werbekampagne zur Neukundengewinnung über Facebook. Sprich ein Bild indem alles kurz und knapp für den Kunden erklärt wird und man damit Werbung schalten kann.

```html
<!DOCTYPE html>
<html lang="de">
<head>
<meta charset="utf-8">
<title>Brötchenservice Werner Lindenau – Anzeige</title>
<link rel="stylesheet" href="https://fonts.googleapis.com/css2?family=Open+Sans:wght@300;700&display=swap">
<style>
  :root {
    --brand-brown: #7a3320;
    --text-brown: #6e2f1f;
    --paper: #ffffff;
    --bread-dark: #8a5a34;
    --bread-mid: #c4834a;
    --bread-light: #e2b27a;
    --badge-fill: #f6c9a0;
  }
  * { margin: 0; padding: 0; box-sizing: border-box; }
  html, body {
    width: 1200px;
    height: 1200px;
    overflow: hidden;
    background: var(--paper);
  }
  .ad {
    position: relative;
    width: 1200px;
    height: 1200px;
    background: var(--paper);
    font-family: "Open Sans", Arial, sans-serif;
    color: var(--text-brown);
    text-align: center;
  }
  .bread-banner {
    position: absolute;
    left: 0;
    top: 0;
    width: 1200px;
    height: 430px;
    background:
      radial-gradient(ellipse 30% 45% at 22% 55%, var(--bread-light), transparent 70%),
      radial-gradient(ellipse 28% 40% at 60% 35%, var(--bread-dark), transparent 70%),
      radial-gradient(ellipse 25% 45% at 88% 60%, var(--bread-light), transparent 70%),
      linear-gradient(90deg, var(--bread-mid), var(--bread-dark) 50%, var(--bread-mid));
    -webkit-mask-image: linear-gradient(to bottom, #000 62%, transparent 100%);
    mask-image: linear-gradient(to bottom, #000 62%, transparent 100%);
  }
  .headline {
    position: absolute;
    left: 0;
    width: 100%;
    font-weight: 700;
    font-size: 75px;
    line-height: 1;
    color: var(--brand-brown);
  }
  .headline--service { top: 405px; }
  .headline--name { top: 497px; }
  .tagline {
    position: absolute;
    top: 610px;
    left: 0;
    width: 100%;
    font-weight: 300;
    font-size: 53px;
    line-height: 1;
  }
  .info {
    position: absolute;
    left: 0;
    width: 100%;
    font-weight: 300;
    font-size: 35px;
    line-height: 40px;
  }
  .info--delivery { top: 690px; }
  .info--order { top: 797px; }
  .info--contact { top: 846px; }
  .info--web { top: 896px; }
  .brand-mark {
    position: absolute;
    left: 544px;
    top: 1002px;
    width: 120px;
    height: 120px;
  }
  .brand-name {
    position: absolute;
    top: 1130px;
    left: 0;
    width: 100%;
    font-weight: 300;
    font-size: 24px;
    line-height: 1;
    color: var(--brand-brown);
  }
</style>
</head>
<body>
  <main class="ad">
    <div class="bread-banner" role="img" aria-label="Foto: Auswahl an frischen Broten, Brötchen, Zopf und Körnern"></div>

    <h1>
      <span class="headline headline--service">Brötchenservice</span>
      <span class="headline headline--name">Werner Lindenau</span>
    </h1>

    <p class="tagline">Ofenfrisches Brot für Sie zu Hause</p>

    <p class="info info--delivery">Lassen Sie sich Ihr Brot und Ihre Brötchen am Freitag, Samstag<br>und Sonntag frisch nach Hause liefern.</p>

    <p class="info info--order">Geben Sie Ihre Bestellung jetzt auf:</p>
    <p class="info info--contact">035841 / 27 63 18 oder kontakt@broetchenservice-kessler.de</p>
    <p class="info info--web">https://www.broetchenservice-kessler.de/</p>

    <svg class="brand-mark" viewBox="0 0 120 120" aria-hidden="true">
      <circle cx="60" cy="60" r="56" fill="var(--badge-fill)" stroke="var(--brand-brown)" stroke-width="4"/>
    </svg>
    <p class="brand-name">Jonas Kessler</p>
  </main>
</body>
</html>
```